Conference for Teenagers Needs Event Graphics

I am in need of event graphics for our upcoming event. This event, titled "Kestrel Youth Rally", is a weekend event for teenagers 11-19 years old. They hear from speakers, listen to a band, and do other fun activities. Our theme is "Together." Graphic design should have a young adult/older teen feel. Clean, not very bright colors.

Event Info:
November 6-8, 2020
Pellworth Exhibit Hall, Brenmoor, NE
Speakers: TBD (will give name and picture before final approval)
Worship: (band name TBD before final approval)
KestrelYouthRally.com
#417KR
Our Organization Logo (attached): Lumen Forward

Once designed, I need the following graphics file sizes:
-11x17 Vertical Poster design: include all event info AND a "blank" spot/box for groups to add their own details/information. Also include the QRV logo and our organization logo Lumen Forward in someway.
-4x3 horizontal postcard: include all event info on 1 side including LumenForward logo and QRV; blank backside
-Main Graphic Slide: formatted to fit a widescreen 16x9 screen. Include event name, hashtag, QRV and Lumen Forward logo
-social media graphics for event: can incorporate some or all of the event details
-4.25x 2.75 vertical badge: include event title on front with Lumen Forward logo

Target Market(s)

Young adults or older teenagers

Requirements
Must have
• -event info
-Lumen Forward Logo & QRV logo

```html
<!DOCTYPE html>
<html lang="en">
<head>
<meta charset="utf-8">
<title>Kestrel Youth Rally – Together We Rise</title>
<link rel="stylesheet" href="https://fonts.googleapis.com/css2?family=Hind:wght@500;600;700&family=Permanent+Marker&display=swap">
<style>
  :root {
    --stage: #6f6f6f;
    --paper: #ffffff;
    --red: #cf1f3c;
    --navy: #283a8f;
    --orange: #f9a930;
    --cyan: #41b6e6;
    --slot: #959595;
    --figure-blue: #6fa3d2;
    --grid: #f9b548;
  }
  * { box-sizing: border-box; margin: 0; padding: 0; }
  html, body { width: 1200px; height: 1200px; overflow: hidden; background: var(--stage); }
  .poster {
    position: absolute; left: 245px; top: 50px; width: 712px; height: 1100px;
    background: var(--paper); overflow: hidden;
    font-family: "Hind", Arial, sans-serif;
  }
  .grid { position: absolute; inset: 0; }
  .brand { position: absolute; font-weight: 700; line-height: 1; }
  .brand-org { left: 27px; top: 42px; font-size: 21px; width: 110px; color: var(--cyan); }
  .brand-partner { right: 24px; top: 46px; font-size: 34px; color: var(--navy); }
  .figure { position: absolute; border-radius: 40% 40% 30% 30%; opacity: .85; }
  .figure-top { left: 380px; top: 75px; width: 135px; height: 110px; background: linear-gradient(135deg, var(--figure-blue), var(--red)); }
  .figure-jump { left: 540px; top: 555px; width: 95px; height: 145px; background: linear-gradient(160deg, var(--cyan), var(--red)); }
  .figure-kneel { left: 17px; top: 775px; width: 123px; height: 150px; background: linear-gradient(160deg, var(--orange), var(--navy)); }
  .figure-dance { left: 610px; top: 930px; width: 75px; height: 110px; background: linear-gradient(160deg, var(--orange), var(--navy)); }
  .title {
    position: absolute; font-family: "Permanent Marker", "Arial Black", sans-serif;
    font-weight: 400; line-height: 1; white-space: nowrap; letter-spacing: -2px;
  }
  .title-together { top: 180px; left: 64px; width: 590px; text-align: center; font-size: 100px; color: var(--red); }
  .title-rise { top: 290px; left: 155px; width: 425px; text-align: center; font-size: 100px; color: var(--navy); text-shadow: 5px 5px 0 var(--orange); }
  .band { position: absolute; display: flex; align-items: center; justify-content: center; font-weight: 600; line-height: 1; }
  .band-name { left: 57px; top: 428px; width: 598px; height: 59px; background: var(--orange); color: var(--navy); font-size: 33px; padding-top: 5px; }
  .band-date { left: 147px; top: 480px; width: 418px; height: 57px; background: var(--navy); color: #fff; font-size: 35px; padding-top: 5px; }
  .guest { position: absolute; top: 645px; width: 210px; text-align: center; }
  .guest-speaker { left: 145px; }
  .guest-worship { left: 375px; }
  .guest-photo {
    width: 210px; height: 210px; margin: 0 auto; border-radius: 50%;
    background: var(--slot); border-top: 5px solid var(--orange); border-left: 3px solid var(--orange);
    display: flex; align-items: center; justify-content: center; color: #fff; font-size: 13px;
  }
  .guest-label {
    position: relative; margin: -40px auto 0; width: 204px; height: 78px; border-radius: 18px;
    background: var(--orange); color: var(--navy); font-size: 15.5px; font-weight: 600; line-height: 19px;
    display: flex; flex-direction: column; justify-content: center; padding-top: 3px;
  }
  .footer {
    position: absolute; left: 0; bottom: 0; width: 100%; height: 106px;
    background: var(--navy); border-top: 5px solid var(--cyan); color: #fff;
  }
  .footer-venue { position: absolute; left: 170px; top: 24px; width: 350px; font-size: 16px; font-weight: 600; letter-spacing: .3px; white-space: nowrap; display: flex; align-items: center; gap: 6px; }
  .footer-web { position: absolute; left: 210px; top: 56px; font-size: 21px; font-weight: 500; white-space: nowrap; display: flex; align-items: center; gap: 6px; }
  .hashtag {
    position: absolute; left: 538px; top: 36px; width: 117px; height: 45px; border-radius: 22px;
    background: var(--orange); color: var(--navy); font-size: 23px; font-weight: 700;
    display: flex; align-items: center; justify-content: center; padding-top: 3px;
  }
</style>
</head>
<body>
<main class="poster">
  <svg class="grid" width="712" height="1100" aria-hidden="true">
    <g stroke="var(--grid)" stroke-width="1.2" fill="none">
      <line x1="175" y1="95" x2="520" y2="40"/>
      <line x1="130" y1="250" x2="600" y2="175"/>
      <line x1="0" y1="370" x2="670" y2="285"/>
      <line x1="60" y1="500" x2="712" y2="410"/>
      <line x1="30" y1="595" x2="712" y2="505"/>
      <line x1="50" y1="720" x2="712" y2="640"/>
      <line x1="80" y1="850" x2="712" y2="770"/>
      <line x1="130" y1="985" x2="712" y2="910"/>
      <line x1="175" y1="95" x2="300" y2="1000"/>
      <line x1="270" y1="80" x2="380" y2="990"/>
      <line x1="360" y1="65" x2="460" y2="980"/>
      <line x1="445" y1="60" x2="545" y2="970"/>
      <line x1="520" y1="40" x2="625" y2="960"/>
      <line x1="80" y1="250" x2="210" y2="990"/>
    </g>
    <circle cx="73" cy="365" r="18" fill="var(--orange)"/>
    <circle cx="67" cy="710" r="13" fill="var(--orange)"/>
  </svg>

  <div class="brand brand-org">Lumen Forward</div>
  <div class="brand brand-partner">QRV</div>

  <div class="figure figure-top" role="img" aria-label="Illustration of a teenager leaping with arms spread"></div>

  <h1 class="title title-together">TOGETHER</h1>
  <h2 class="title title-rise">WE RISE</h2>

  <div class="band band-name">KESTREL YOUTH RALLY</div>
  <div class="band band-date">NOVEMBER 6-8, 2020</div>

  <div class="figure figure-jump" role="img" aria-label="Illustration of a teenager jumping with arms raised"></div>

  <section class="guest guest-speaker">
    <div class="guest-photo">picture</div>
    <div class="guest-label"><span>Speaker</span><span>Name</span><span>Association</span></div>
  </section>
  <section class="guest guest-worship">
    <div class="guest-photo">picture</div>
    <div class="guest-label"><span>Worship</span><span>Name</span><span>Association</span></div>
  </section>

  <div class="figure figure-kneel" role="img" aria-label="Illustration of a kneeling teenager waving"></div>
  <div class="figure figure-dance" role="img" aria-label="Illustration of a teenager dancing"></div>

  <footer class="footer">
    <div class="footer-venue">
      <svg width="17" height="17" viewBox="0 0 20 20" aria-hidden="true"><circle cx="10" cy="10" r="8.5" fill="none" stroke="#fff" stroke-width="2"/><path d="M5 10.5 10 6l5 4.5V14H5z" fill="#fff"/></svg>
      PELLWORTH EXHIBIT HALL, BRENMOOR, NE
    </div>
    <div class="footer-web">
      <svg width="17" height="17" viewBox="0 0 20 20" aria-hidden="true"><g fill="none" stroke="#fff" stroke-width="1.6"><circle cx="10" cy="10" r="8.5"/><ellipse cx="10" cy="10" rx="3.8" ry="8.5"/><line x1="1.5" y1="10" x2="18.5" y2="10"/></g></svg>
      KestrelYouthRally.com
    </div>
    <div class="hashtag">#417KR</div>
  </footer>
</main>
</body>
</html>
```